WTF!!! We need a modern professional website for a business litigation law firm.

We need a modern, clean, professional and uncomplicated website for a new business trial and litigation law firm called "Harrowgate Trial Firm PLLC". Website must be mobile optimized for iPad and smartphone. The law firm specializes in counseling and representing large corporations, small businesses and entrepreneurs in and out of the courtroom. Lawyers in the firm serve as Florida counsel and trial counsel to organizations facing claims involving product liability, premises liability, professional liability, vehicle and transportation liability, warranty claims, construction defects and delay claims, complex business disputes, commercial litigation and bid disputes in State and Federal Courts. The website is mainly to provide information about the firm, and should include sections describing the firm, identifying the Industries Served and Areas of Practice ," a separate page identifying the "Professionals", a separate page for "Resources & Advisories," and a traveling "Connect With Us" button a site visitor can click on that will launch an email to the Firm's general email account. The website should allow us to easily modify the content on these pages, and let us add/modify links to external information sources. We will not sell anything or take payments through the website. We do need to be able to easily upload and update photographs of attorneys and add new attorneys names/email hyperlinks as the firm grows. We would like to add developments in the law or success stories easily and quickly, such as through a blog page. On the "Connect With Us" page the website should have hyperlinks to email the Firm, and there should be hyperlinks to email each professional on the "Professionals" page. The website should be viewable on mobile devices without distortion. The law firm focuses on trial work and should have some imagery associated with courtrooms, but the overall theme of the site should be modern, clean, and communicate sophistication and strength. The website should be made in Wordpress. We have uploaded logo files for Harrowgate Trial Firm.

Target Market(s)

Corporations and companies that are looking for legal representation. Other attorneys/legal industry.

Industry/Entity Type

Legal Industry

Coding

Coded - Design and coding required

Number of Pages Required

1 page

Font styles to use
Sans Serif

Requirements
Must have
• Simple, clean, sophisticated, modern website that includes the logo, watermark of logo, and the elements described above.
Nice to have
• Pictures of city scape, buildings, courtroom, team members.

```html
<!DOCTYPE html>
<html lang="en">
<head>
<meta charset="utf-8">
<title>Harrowgate Trial Firm</title>
<link href="https://fonts.googleapis.com/css2?family=Montserrat:wght@400;500;600;700&display=swap" rel="stylesheet">
<style>
:root{
  --teal:#1b9cb1;
  --ink:#1d1d1f;
  --muted:#6b6b6b;
  --line:#e2e2e2;
  --white:#ffffff;
  --black:#000000;
}
*{box-sizing:border-box;margin:0;padding:0}
html,body{width:1200px;height:3461px;overflow:hidden}
body{position:relative;font-family:'Montserrat',sans-serif;color:var(--ink);background:var(--white)}
.abs{position:absolute}
a{color:inherit;text-decoration:none}

/* hero */
.hero{left:0;top:0;width:1200px;height:629px;background:linear-gradient(100deg,#3a2a1f 0%,#6a5846 35%,#4b4a4e 60%,#2a2e3a 100%)}
.hero-shade{left:0;top:0;width:1200px;height:629px;background:linear-gradient(90deg,rgba(0,0,0,.45),rgba(0,0,0,.05))}
.brand{color:var(--white);font-weight:700;font-size:24px;line-height:28px;letter-spacing:.5px}
.brand small{display:block;font-size:12px;letter-spacing:3px;font-weight:700}
.nav{top:36px;left:364px;display:flex;gap:0;font-size:15px;color:var(--white)}
.nav span{position:absolute;white-space:nowrap}
.nav .active{font-weight:700}
.nav .active::after{content:"";position:absolute;left:0;right:0;top:26px;height:3px;background:var(--teal)}
.hero-title{left:112px;top:276px;font-size:44px;line-height:53px;font-weight:600;color:var(--white)}
.btn{background:var(--teal);color:var(--white);font-weight:600;font-size:16px;display:flex;align-items:center;justify-content:center;gap:4px}
.dot{width:16px;height:16px;border-radius:50%;border:2px solid var(--white)}
.dot.on{background:var(--white)}

/* headings */
.eyebrow{font-size:21px;color:var(--teal);font-weight:400}
.h2{font-size:36px;font-weight:500;color:var(--ink)}
.lede{font-size:15.5px;line-height:23px;color:var(--muted)}
.arrow-box{width:49px;height:50px;border:1.5px solid #333;display:flex;align-items:center;justify-content:center;background:var(--white)}
.arrow-box.fill{background:var(--teal);border-color:var(--teal)}

/* practice cards */
.card{top:890px;width:225px;height:298px;border:2px solid var(--line);border-radius:16px;text-align:center}
.card .icon{width:108px;height:108px;border-radius:50%;background:var(--teal);margin:19px auto 0}
.card h3{font-size:19px;font-weight:500;margin-top:18px}
.card p{font-size:13px;line-height:19px;color:var(--muted);margin:10px 14px 0}
.card a{display:block;color:var(--teal);font-weight:600;font-size:15px;margin-top:22px}

/* who */
.who-photo{left:0;top:1274px;width:546px;height:558px;background:linear-gradient(135deg,#3a3f55,#7a5a42 55,#c9a27c)}
.who-panel{left:546px;top:1274px;width:654px;height:558px;background:linear-gradient(180deg,#2a3238,#1f2a33)}
.who-text{left:626px;color:var(--white)}

/* industries */
.ind-photo{top:2095px;width:264px;height:261px}
.ind-label{top:2330px;width:266px;height:53px;background:var(--black);color:var(--white);font-size:19px;display:flex;align-items:center;justify-content:center}
.ind-label.hl{background:var(--teal);box-shadow:0 4px 10px rgba(0,0,0,.35)}

/* testimonials */
.stories{left:0;top:2469px;width:1200px;height:705px;background:linear-gradient(110deg,#1e1a17 0%,#4a3a2c 45%,#3a2c22 75%,#5a4a3a 100%)}
.center{left:0;width:1200px;text-align:center;color:var(--white)}
.quote-card{left:144px;top:2818px;width:914px;height:210px;background:var(--white)}
.avatar{left:533px;top:2735px;width:134px;height:134px;border-radius:50%;background:linear-gradient(160deg,#d8dde3,#8ea3b8);border:3px solid var(--white)}

/* footer */
.footer{left:0;top:3174px;width:1200px;height:287px;background:var(--black);color:var(--white)}
.foot-nav{top:3364px;left:0;width:1200px;display:flex;justify-content:center;gap:29px;font-size:16px;color:var(--white)}
.foot-rule{left:0;top:3407px;width:1200px;height:1px;background:#444}
.copy{top:3417px;left:0;width:1200px;text-align:center;font-size:12px;color:var(--white)}
</style>
</head>
<body>

<!-- Hero -->
<div class="abs hero" role="img" aria-label="Photo of three lawyers reviewing documents at a meeting table"></div>
<div class="abs hero-shade"></div>
<div class="abs brand" style="left:112px;top:68px">HARROWGATE<small>TRIAL FIRM</small></div>
<nav class="abs nav">
  <span class="active" style="left:0">Home</span>
  <span style="left:78px">About Us</span>
  <span style="left:177px">Practice Areas</span>
  <span style="left:316px">Professionals</span>
  <span style="left:445px">Industries Served</span>
  <span style="left:607px">Blog</span>
  <span style="left:672px">More ⌄</span>
</nav>
<h1 class="abs hero-title">Trial Counsel for Complex<br>Legal Challenges</h1>
<a class="abs btn" style="left:112px;top:413px;width:186px;height:36px">Connect With Us →</a>
<div class="abs dot on" style="left:562px;top:559px"></div>
<div class="abs dot" style="left:592px;top:559px"></div>
<div class="abs dot" style="left:622px;top:559px"></div>

<!-- Practice areas -->
<div class="abs eyebrow" style="left:112px;top:706px">WHAT WE DO</div>
<h2 class="abs h2" style="left:111px;top:751px">Our Practice Areas</h2>
<p class="abs lede" style="left:112px;top:804px">Lorem ipsum dolor sit amet, consectetur adipiscing elit, sed do eiusmod<br>tempor incididunt ut&nbsp; labore et dolore magna aliqua.</p>
<div class="abs arrow-box" style="left:953px;top:755px"><svg width="14" height="22" viewBox="0 0 14 22"><path d="M11 2 3 11l8 9" fill="none" stroke="#222" stroke-width="2"/></svg></div>
<div class="abs arrow-box fill" style="left:1039px;top:755px"><svg width="14" height="22" viewBox="0 0 14 22"><path d="M3 2l8 9-8 9" fill="none" stroke="#fff" stroke-width="2"/></svg></div>

<div class="abs card" style="left:112px"><div class="icon" role="img" aria-label="Product liability icon"></div><h3>Product Liability</h3><p>Lorem ipsum dolor sit amet, consectetur adipiscing elit, sed do eiusmod</p><a>Read More →</a></div>
<div class="abs card" style="left:363px"><div class="icon" role="img" aria-label="Premises liability icon"></div><h3>Premises Liability</h3><p>Lorem ipsum dolor sit amet, consectetur adipiscing elit, sed do eiusmod</p><a>Read More →</a></div>
<div class="abs card" style="left:613px"><div class="icon" role="img" aria-label="Warranty claims icon"></div><h3>Warranty Claims</h3><p>Lorem ipsum dolor sit amet, consectetur adipiscing elit, sed do eiusmod</p><a>Read More →</a></div>
<div class="abs card" style="left:864px"><div class="icon" role="img" aria-label="Professional liability icon"></div><h3>Professional Liability</h3><p>Lorem ipsum dolor sit amet, consectetur adipiscing elit, sed do eiusmod</p><a>Read More →</a></div>

<!-- Who we are -->
<div class="abs who-photo" role="img" aria-label="Photo of attorneys in conversation in an office"></div>
<div class="abs who-panel" role="img" aria-label="Dim photo of a team meeting behind a dark overlay"></div>
<div class="abs who-text" style="top:1358px;font-size:21px">WHO WE ARE</div>
<h2 class="abs who-text" style="top:1403px;font-size:38px;line-height:44px;font-weight:500">Leading Advocates in<br>Trial Law</h2>
<p class="abs who-text" style="top:1503px;width:480px;font-size:15.5px;line-height:23.2px">Sed ut perspiciatis unde omnis iste natus error sit voluptatem accusantium doloremque laudantium, totam rem aperiam, eaque ipsa quae ab illo inventore veritatis et quasi architecto beatae vitae dicta sunt explicabo. Nemo enim ipsam voluptatem quia voluptas sit aspernatur aut odit aut fugit, sed quia consequuntur magni dolores eos qui ratione voluptatem sequi nesciunt.</p>
<a class="abs btn" style="left:626px;top:1684px;width:152px;height:36px">Read More →</a>

<!-- Industries -->
<div class="abs eyebrow" style="left:112px;top:1914px">INDUSTRIES SERVE</div>
<h2 class="abs h2" style="left:111px;top:1959px">Legal Expertise Across Industries</h2>
<p class="abs lede" style="left:112px;top:2012px">Lorem ipsum dolor sit amet, consectetur adipiscing elit, sed do eiusmod<br>tempor incididunt ut&nbsp; labore et dolore magna aliqua.</p>
<div class="abs arrow-box" style="left:952px;top:1966px"><svg width="14" height="22" viewBox="0 0 14 22"><path d="M11 2 3 11l8 9" fill="none" stroke="#222" stroke-width="2"/></svg></div>
<div class="abs arrow-box" style="left:1038px;top:1966px"><svg width="14" height="22" viewBox="0 0 14 22"><path d="M3 2l8 9-8 9" fill="none" stroke="#222" stroke-width="2"/></svg></div>

<div class="abs ind-photo" style="left:116px;background:linear-gradient(160deg,#c9d3dc,#56606b)" role="img" aria-label="Photo of engineers with a laptop in a factory"></div>
<div class="abs ind-label" style="left:137px">Lorem ipsum dolor</div>
<div class="abs ind-photo" style="left:453px;background:linear-gradient(160deg,#2b3440,#a07a2a 70%,#1c2128);box-shadow:0 4px 10px rgba(0,0,0,.35)" role="img" aria-label="Photo of a technician beside an industrial robot arm"></div>
<div class="abs ind-label hl" style="left:480px">Lorem ipsum dolor</div>
<div class="abs ind-photo" style="left:796px;background:linear-gradient(160deg,#e8e4de,#8c7a66)" role="img" aria-label="Photo of two workers with a tablet in a warehouse"></div>
<div class="abs ind-label" style="left:822px">Lorem ipsum dolor</div>

<!-- Testimonials -->
<div class="abs stories" role="img" aria-label="Photo of a hand signing documents beside courthouse columns, darkened"></div>
<div class="abs center" style="top:2551px;font-size:21px">SUCCESS STORIES</div>
<h2 class="abs center" style="top:2596px;font-size:36px;font-weight:500">What Our Clients Say</h2>
<p class="abs center" style="top:2650px;font-size:15.5px;line-height:23px">Lorem ipsum dolor sit amet, consectetur adipiscing elit, sed do eiusmod tempor incididunt<br>ut&nbsp; labore et dolore magna aliqua.</p>
<div class="abs quote-card"></div>
<svg class="abs" style="left:223px;top:2842px" width="62" height="52" viewBox="0 0 62 52"><path d="M0 26C0 10 8 2 24 0v10c-8 2-11 6-11 12h11v30H0zM36 26C36 10 44 2 60 0v10c-8 2-11 6-11 12h11v30H36z" fill="#1b9cb1"/></svg>
<div class="abs avatar" role="img" aria-label="Client portrait"></div>
<p class="abs" style="left:144px;top:2892px;width:914px;text-align:center;font-size:15.5px;line-height:23.5px;color:#333">Lorem ipsum dolor sit amet, consectetur adipiscing elit,<br>sed do eiusmod tempor incididunt ut labore et dolore magna aliqua. Ut enim ad minim veniam,<br>quis nostrud exercitation ullamco laboris nisi ut aliquip ex</p>
<div class="abs" style="left:144px;top:2984px;width:914px;text-align:center;font-size:20px;font-weight:600;color:var(--teal)">Daniel Mercer</div>
<div class="abs dot on" style="left:562px;top:3069px"></div>
<div class="abs dot" style="left:592px;top:3069px"></div>
<div class="abs dot" style="left:622px;top:3069px"></div>

<!-- Footer -->
<footer class="abs footer"></footer>
<div class="abs brand" style="left:0;top:3262px;width:1200px;text-align:center;font-size:30px;line-height:34px">HARROWGATE<small style="font-size:14px;letter-spacing:4px">TRIAL FIRM</small></div>
<nav class="abs foot-nav"><span>Home</span><span>About</span><span>Practice Areas</span><span>Professionals</span><span>Industries Served</span><span>Blog</span><span>Resources &amp; Advisories</span><span>Contact</span></nav>
<div class="abs foot-rule"></div>
<div class="abs copy">Copyright 2025, Harrowgate Trial Firm PLLC. All Rights Reserved.</div>

</body>
</html>
```